Refresh Brightwave Coursecraft

Need a new design for e-learning development and web app development site: http://brightwavecoursecraft.example. Need pages for everything on menu bar plus a training services and a web app development services pages and a better page for samples http://brightwavecoursecraft.example/samples5/.

***Must be programmed in html 5. NO CMS. No WP. No Pillar. Straight html/css.

Target Market(s)

government

Industry/Entity Type

Government

Coding

Coded - Design and coding required

Number of Pages Required

1 page

Requirements
Must have
• Must be coded in html5/css. No CMS.
• Divided so you can easily see that we offer 3 separate services:
• Live Training - E-Learning Development - Web App Development
• A way to display logos of all our clients like on bottom of this page: https://www.quorvatests.example (this is also our website so you can copy all these logos)
• List both our Denver location which is already on our website plus our office in Veltoma Plaza. Street 62 Este, 17-83. Medellín, Antioquia.
• A page like this for our web app dev services https://www.zelbrax.example/product-development
Should not have
• CMS

```html
<!DOCTYPE html>
<html lang="en">
<head>
<meta charset="utf-8">
<title>Brightwave Coursecraft Solutions</title>
<link href="https://fonts.googleapis.com/css2?family=Poppins:wght@300;400;500;600;700&family=Open+Sans:wght@400;600&display=swap" rel="stylesheet">
<style>
:root{
  --blue:#1a8ac9;
  --orange:#f7a733;
  --ink:#1f1f1f;
  --muted:#8a8a8a;
  --line:#e4e4e4;
  --soft:#f4f4f4;
  --dark:#222831;
  --white:#ffffff;
}
*{box-sizing:border-box;margin:0;padding:0}
html,body{width:1200px;height:3543px;overflow:hidden}
body{position:relative;font-family:"Open Sans",Arial,sans-serif;color:var(--ink);background:var(--white)}
.abs{position:absolute}
h1,h2,h3,h4,.heading{font-family:"Poppins",Arial,sans-serif}

/* header */
.site-header{left:0;top:0;width:1200px;height:82px;background:var(--white);border-bottom:3px solid var(--orange)}
.brand{left:161px;top:18px;display:flex;align-items:center;gap:10px;font-family:"Poppins",sans-serif;font-weight:600;font-size:19px;color:var(--blue)}
.brand-dot{width:36px;height:36px;border-radius:50%;background:var(--orange)}
.main-nav{right:150px;top:0;display:flex;height:79px;font-family:"Poppins",sans-serif;font-size:12px;color:#666;text-transform:uppercase}
.main-nav span{display:flex;align-items:center;padding:0 13px}
.main-nav .active{background:var(--orange);color:var(--white)}

/* hero */
.hero{left:0;top:82px;width:1200px;height:518px;background:linear-gradient(120deg,#3c3f44,#7b7a78 55%,#a09a92)}
.hero-shade{left:0;top:82px;width:1200px;height:518px;background:rgba(0,0,0,.35)}
.hero-copy{left:0;top:268px;width:1200px;text-align:center;color:var(--white)}
.hero-kicker{font-family:"Poppins",sans-serif;letter-spacing:3px;font-size:15px}
.hero-title{font-size:29px;font-weight:600;line-height:36px;margin-top:8px}
.btn-ghost{display:inline-block;margin-top:26px;border:1px solid var(--white);border-radius:20px;padding:7px 24px;font-size:11px;font-family:"Poppins",sans-serif}
.hero-arrow{top:322px;width:34px;height:34px;border-radius:50%;border:1px solid var(--white);display:flex;align-items:center;justify-content:center}

/* section titles */
.section-head{left:0;width:1200px;text-align:center}
.section-kicker{font-size:11px;color:var(--muted);text-transform:uppercase;letter-spacing:.5px}
.section-title{font-size:25px;font-weight:600;margin-top:6px}
.title-rule{width:30px;height:2px;background:var(--orange);margin:12px auto 0}

/* services */
.services{left:161px;top:763px;width:876px;height:229px;display:flex;border:1px solid var(--line)}
.service{flex:1;text-align:center;padding:26px 30px 0;border-right:1px solid var(--line)}
.service:last-child{border-right:0}
.service.featured{background:var(--blue);color:var(--white)}
.service-icon{width:52px;height:52px;margin:0 auto}
.service h3{font-size:15px;font-weight:600;margin-top:16px;text-transform:uppercase}
.service p{font-size:11px;line-height:17px;color:var(--muted);margin-top:10px}
.service.featured p{color:#e6f2fa}
.service .more{font-size:10px;font-weight:600;margin-top:12px}

/* about */
.about{left:0;top:1053px;width:1200px;height:482px;background:var(--soft)}
.about-photo{left:0;top:1053px;width:364px;height:367px;background:linear-gradient(135deg,#6d6a54,#a69a6e 55%,#3c8fbf)}
.about-copy{left:437px;top:1110px;width:605px}
.about-copy h2{font-size:25px;font-weight:600;line-height:32px;margin-top:8px}
.about-copy p{font-size:11.5px;line-height:21px;color:var(--muted);margin-top:20px}
.about-copy strong{color:var(--ink);font-weight:600}
.btn-outline{display:inline-block;margin-top:32px;border:1px solid var(--orange);color:var(--orange);border-radius:16px;padding:5px 20px;font-size:11px}

/* team */
.team-band{left:0;top:1613px;width:1200px;height:291px;background:var(--blue)}
.team-intro{left:161px;top:1670px;width:280px;color:var(--white)}
.team-intro h2{font-size:25px;font-weight:600;margin-top:6px}
.team-intro p{font-size:11px;line-height:18px;margin-top:18px;color:#dcecf7}
.team-arrows{display:flex;gap:8px;margin-top:22px}
.team-arrows span{width:26px;height:26px;border-radius:50%;border:1px solid var(--white);display:flex;align-items:center;justify-content:center}
.member{top:1601px;width:170px;height:237px;background:var(--white);border-radius:8px;overflow:hidden}
.member-photo{height:180px;background:linear-gradient(180deg,#c9c9c9,#8f8f8f)}
.member-info{padding:10px 14px;font-size:13px;font-family:"Poppins",sans-serif;font-weight:600}
.member-info small{display:block;font-size:10px;color:var(--orange);font-weight:400}
.member.active .member-info{background:var(--orange);color:var(--white);height:57px}
.member.active small{color:var(--white)}

/* clients */
.clients{left:161px;top:2071px;width:876px;display:grid;grid-template-columns:repeat(6,1fr);border-top:1px solid var(--line);border-left:1px solid var(--line)}
.client{height:98px;border-right:1px solid var(--line);border-bottom:1px solid var(--line);display:flex;align-items:center;justify-content:center;gap:6px;font-family:"Poppins",sans-serif;font-size:11px;font-weight:600;color:#4a5a75;text-align:center;padding:0 6px}
.client i{width:12px;height:12px;border-radius:50%;background:#4a5a75;flex:none}

/* contracts */
.consult{left:0;top:2420px;width:1200px;text-align:center;font-family:"Poppins",sans-serif;font-weight:600;font-size:16px}
.contracts{left:161px;top:2470px;width:876px;border-collapse:collapse;font-size:11px;color:var(--muted)}
.contracts th{background:#ececec;color:var(--ink);font-weight:600;height:44px;font-size:11px}
.contracts td{height:44px;text-align:center;border:1px solid var(--line)}

/* contact */
.contact-bg{left:0;top:2770px;width:1200px;height:572px;background:linear-gradient(120deg,#2a2f35,#3a3a36 60%,#24292e);clip-path:polygon(0 32%,100% 0,100% 100%,0 100%)}
.contact-head{left:161px;top:2752px;width:352px;height:118px;background:var(--orange);color:var(--white);padding:26px 28px}
.contact-head h2{font-size:25px;font-weight:600}
.contact-head p{font-size:11px;line-height:17px;margin-top:6px}
.contact-form{left:161px;top:2870px;width:352px;height:397px;background:var(--white);padding:40px 30px;box-shadow:0 4px 18px rgba(0,0,0,.15)}
.field{height:36px;border:1px solid var(--line);margin-bottom:14px;font-size:11px;color:#999;padding:10px 12px}
.field.tall{height:90px}
.btn-submit{height:36px;background:var(--blue);color:var(--white);font-size:11px;font-weight:600;display:flex;align-items:center;justify-content:center;margin-top:6px}
.office{color:var(--white);width:230px}
.office h4{font-size:16px;font-weight:600;margin-bottom:12px}
.office-line{display:flex;gap:10px;font-size:11px;line-height:17px;margin-bottom:10px}
.office-line svg{flex:none;margin-top:2px}
.office .phone{color:var(--orange);font-weight:600;font-size:15px}

/* footer */
.footer-brand{left:161px;top:3405px}
.footer-col{top:3398px;font-size:11px;line-height:26px;color:var(--muted)}
.footer-col .hl{color:var(--orange)}
.footer-col h4{font-size:11px;color:var(--ink);font-weight:600}
.social{display:flex;gap:10px;margin-top:6px}
.social span{width:26px;height:26px;border-radius:50%;border:1px solid var(--line)}
.social span:first-child{background:var(--orange);border-color:var(--orange)}
.copyright{left:0;top:3496px;width:1200px;height:47px;border-top:1px solid var(--line);text-align:center;font-size:10px;color:var(--muted);line-height:47px}
</style>
</head>
<body>

<header class="site-header abs">
  <div class="brand abs"><span class="brand-dot"></span>Brightwave Coursecraft</div>
  <nav class="main-nav abs">
    <span class="active">Home</span><span>Who We Are</span><span>Featured Services</span><span>Portfolio</span><span>Team &amp; Experience</span><span>Contact Us</span>
  </nav>
</header>

<section>
  <div class="hero abs" role="img" aria-label="Hands typing on a laptop keyboard"></div>
  <div class="hero-shade abs"></div>
  <div class="hero-copy abs">
    <div class="hero-kicker">WE PROVIDE</div>
    <h1 class="hero-title">ENGAGING TRAINING THAT<br>EXCEED EXPECTATIONS.</h1>
    <span class="btn-ghost">CONTACT US</span>
  </div>
  <div class="hero-arrow abs" style="left:60px"><svg width="10" height="10" viewBox="0 0 10 10"><path d="M7 1 3 5l4 4" stroke="#fff" fill="none" stroke-width="1.5"/></svg></div>
  <div class="hero-arrow abs" style="left:1106px;background:#fff"><svg width="10" height="10" viewBox="0 0 10 10"><path d="M3 1l4 4-4 4" stroke="#333" fill="none" stroke-width="1.5"/></svg></div>
</section>

<div class="section-head abs" style="top:656px">
  <div class="section-kicker">Featured Services</div>
  <h2 class="section-title">Our Top Services</h2>
  <div class="title-rule"></div>
</div>

<section class="services abs">
  <article class="service featured">
    <svg class="service-icon" viewBox="0 0 52 52"><circle cx="26" cy="26" r="25" fill="#fff"/><circle cx="26" cy="20" r="7" fill="#1a8ac9"/><path d="M14 40c2-8 22-8 24 0z" fill="#1a8ac9"/></svg>
    <h3>Live Training</h3>
    <p>Lorem ipsum dolor sit amet, consectetur adipiscing elit, sed do eiusmod tempor incididunt ut labore et dolore</p>
    <div class="more">Read More</div>
  </article>
  <article class="service">
    <svg class="service-icon" viewBox="0 0 52 52"><rect x="8" y="20" width="36" height="22" fill="#1a8ac9"/><circle cx="26" cy="12" r="6" fill="#f7a733"/><rect x="14" y="25" width="24" height="12" fill="#fff"/></svg>
    <h3>E-Learning Development</h3>
    <p>Lorem ipsum dolor sit amet, consectetur adipiscing elit, sed do eiusmod tempor incididunt ut labore et dolore</p>
    <div class="more">Read More</div>
  </article>
  <article class="service">
    <svg class="service-icon" viewBox="0 0 52 52"><rect x="15" y="4" width="22" height="44" rx="4" fill="#1a8ac9"/><rect x="18" y="10" width="16" height="30" fill="#f7a733"/></svg>
    <h3>Web App Development</h3>
    <p>Lorem ipsum dolor sit amet, consectetur adipiscing elit, sed do eiusmod tempor incididunt ut labore et dolore</p>
    <div class="more">Read More</div>
  </article>
</section>

<section>
  <div class="about abs"></div>
  <div class="about-photo abs" role="img" aria-label="Overhead view of a person working on a laptop at a desk"></div>
  <div class="about-copy abs">
    <div class="section-kicker">Who We Are</div>
    <h2>Instructional Design and Courseware Development Firm</h2>
    <p>Brightwave Coursecraft Solutions (Brightwave Coursecraft) is a Certified, SBA 8(a) Certified, Native American Owned Small Disadvantaged Business located in Denver, Colorado. We have designed and delivered <strong>SCORM compliant eLearning, webinar, web-based training (WBT), instructor-led training (ILT), virtual ILT (vILT), blended, and 3D immersive training courses</strong>. The Instructional Design Team brings nearly one hundred years of Instructional Design experience. Our Instructional Designers have experience designing, developing, and delivering custom technical and business skill training courses. This encompasses a variety of industries, including pharmaceuticals, financial, real estate/property management, health care, telecommunications, financial, real estate/property management, health care, telecommunications, financial, government, oil and gas, software/technology.</p>
    <span class="btn-outline">Read More</span>
  </div>
</section>

<section>
  <div class="team-band abs"></div>
  <div class="team-intro abs">
    <div class="section-kicker" style="color:#dcecf7">Experienced Team</div>
    <h2>Meet Our Team</h2>
    <p>Duis aute irure dolor in reprehenderit in voluptate velit esse cillum dolore eu fugiat nulla pariatur. Excepteur sint occaecat cupidatat non proident.</p>
    <div class="team-arrows">
      <span><svg width="8" height="8" viewBox="0 0 10 10"><path d="M7 1 3 5l4 4" stroke="#fff" fill="none" stroke-width="1.8"/></svg></span>
      <span><svg width="8" height="8" viewBox="0 0 10 10"><path d="M3 1l4 4-4 4" stroke="#fff" fill="none" stroke-width="1.8"/></svg></span>
    </div>
  </div>
  <div class="member active abs" style="left:463px"><div class="member-photo" role="img" aria-label="Portrait of a team member"></div><div class="member-info">Member Name<small>Experience</small></div></div>
  <div class="member abs" style="left:652px"><div class="member-photo" role="img" aria-label="Portrait of a team member"></div><div class="member-info">Member Name<small>Experience</small></div></div>
  <div class="member abs" style="left:841px"><div class="member-photo" role="img" aria-label="Portrait of a team member"></div><div class="member-info">Member Name<small>Experience</small></div></div>
  <div class="member abs" style="left:1030px"><div class="member-photo" role="img" aria-label="Portrait of a team member"></div><div class="member-info">Member Name<small>Experience</small></div></div>
</section>

<div class="section-head abs" style="top:1960px">
  <div class="section-kicker">Featured Clients</div>
  <h2 class="section-title">A Few Of Our Clients</h2>
  <div class="title-rule"></div>
</div>

<section class="clients abs">
  <div class="client"><i></i>Aerial Corps</div>
  <div class="client"><i></i>Ridgeline University</div>
  <div class="client"><i></i>Harlow Institute</div>
  <div class="client"><i></i>Workpath Program</div>
  <div class="client"><i></i>Eastmoor College</div>
  <div class="client"><i></i>Clearmed</div>
  <div class="client"><i></i>Solvanta</div>
  <div class="client"><i></i>Front Range Tech</div>
  <div class="client"><i></i>Lakeside Academy</div>
  <div class="client"><i></i>Harborcrest</div>
  <div class="client"><i></i>Greenvale University</div>
  <div class="client"><i></i>Oakmere School</div>
  <div class="client"><i></i>Kestrel Seminary</div>
  <div class="client"><i></i>Bayfield College</div>
  <div class="client"><i></i>Prairie State</div>
  <div class="client"><i></i>Mountain Ridge College</div>
  <div class="client"><i></i>Northgate Univ.</div>
  <div class="client"><i></i>Summit Fire Academy</div>
</section>

<div class="consult abs">Contact Us Today for a Free Consultation 888-555-0142 x704</div>
<table class="contracts abs">
  <tr><th>Most Common Labor Categories</th><th>Contract Information</th><th>Contract Vehicles</th></tr>
  <tr><td>Instructional Designer</td><td>CAGE code 4QX19</td><td>SBA 8(a) Case Number 410728</td></tr>
  <tr><td>E-learning Project Manager</td><td>GSA PSS Schedule 00-RT-1182</td><td>Certified Small Business</td></tr>
  <tr><td>Graphic Designer</td><td>Primary NAICS 611430 Professional Development Training</td><td>GSA PSS Schedule 00-RT-1182</td></tr>
  <tr><td>Webinar Producer</td><td>541511 541512 541519 611420 611710</td><td>Native American owned</td></tr>
</table>

<section>
  <div class="contact-bg abs" role="img" aria-label="Dimmed photo of a person working at a laptop"></div>
  <div class="contact-head abs">
    <h2>Contact Us</h2>
    <p>Sed ut perspiciatis unde omnis iste natus error sit voluptatem accusantium doloremque</p>
  </div>
  <form class="contact-form abs">
    <div class="field">Your Name</div>
    <div class="field">Your Email</div>
    <div class="field">Phone</div>
    <div class="field tall">Message</div>
    <div class="btn-submit">SUBMIT</div>
  </form>
  <div class="office abs" style="left:633px;top:2925px">
    <h4>Aurora</h4>
    <div class="office-line"><svg width="11" height="14" viewBox="0 0 11 14"><path d="M5.5 0C2.5 0 0 2.4 0 5.4 0 9.5 5.5 14 5.5 14S11 9.5 11 5.4C11 2.4 8.5 0 5.5 0z" fill="#fff"/><circle cx="5.5" cy="5.4" r="2" fill="#333"/></svg>5820 E 9th Avenue, Suite 2-140,<br>CO 80012</div>
    <div class="office-line"><svg width="13" height="13" viewBox="0 0 13 13"><path d="M3 0l2 3-1.5 1.5a8 8 0 0 0 5 5L10 8l3 2-1.5 2.5C6 12.5.5 7 .5 1.5z" fill="#fff"/></svg><span class="phone">+1 888 555 0142</span></div>
    <div class="office-line"><svg width="14" height="10" viewBox="0 0 14 10"><rect x=".5" y=".5" width="13" height="9" fill="none" stroke="#fff"/><path d="M.5.5 7 6l6.5-5.5" fill="none" stroke="#fff"/></svg>support@brightwavecoursecraft.example</div>
    <h4 style="margin-top:26px">Address III</h4>
    <div class="office-line"><svg width="11" height="14" viewBox="0 0 11 14"><path d="M5.5 0C2.5 0 0 2.4 0 5.4 0 9.5 5.5 14 5.5 14S11 9.5 11 5.4C11 2.4 8.5 0 5.5 0z" fill="#fff"/><circle cx="5.5" cy="5.4" r="2" fill="#333"/></svg>Lorem 30 dec, 51-85, omnis,<br>voluptatem</div>
  </div>
  <div class="office abs" style="left:881px;top:2925px">
    <h4>Veltoma Plaza</h4>
    <div class="office-line"><svg width="11" height="14" viewBox="0 0 11 14"><path d="M5.5 0C2.5 0 0 2.4 0 5.4 0 9.5 5.5 14 5.5 14S11 9.5 11 5.4C11 2.4 8.5 0 5.5 0z" fill="#fff"/><circle cx="5.5" cy="5.4" r="2" fill="#333"/></svg>Street 62 Este, 17-83. Medellín,<br>Antioquia</div>
  </div>
</section>

<footer>
  <div class="brand footer-brand abs"><span class="brand-dot"></span>Brightwave Coursecraft</div>
  <div class="footer-col abs" style="left:461px"><div class="hl">About Us</div><div>Privacy Policy</div></div>
  <div class="footer-col abs" style="left:664px"><div>Terms of Services</div><div>Contact Us</div></div>
  <div class="footer-col abs" style="left:836px"><h4>Connect With Us</h4><div class="social"><span></span><span></span><span></span></div></div>
  <div class="copyright abs">© 2019 Brightwave Coursecraft Solution | All Rights Reserved. Design By Northpeak Studio Inc.</div>
</footer>

</body>
</html>
```